Briefpapier und Visitenkarten für Bayerisches Gasthaus mit Zimmer
Zielgruppe
Traditionelle Gaststätte im Zentrum einer Kleinstadt in Bayern. Direkt am Marktplatz. 10 Gästezimmer.
Bayerisch. Traditionell. Von junger Geschäftsführerin geführt, mit jungem Personal. Wir haben das Objekt erst vor Kurzem erworben und fangen gerade an.
Gerichte: Braten, Steaks, Brotzeiten, vegetarische und VEGANE Speisen
Getränke: Sehr bierlastig. Es war früher ein Brauereigasthaus. Heute gibts auch eine kleine feine Weinkarte.
Zielgruppe sind Einheimische und Touristen. Im Sommer kommen Radfahrer und Wanderer. Besonders angesprochen werden auch Kinder. Es gibt eine großzügige Spielecke.
Aufgabenstellung
Das Gasthaus heißt Eichel. Daher spielt der Eichel im Design auch eine wichtige Rolle.
Nachdem wir sehr familienorientiert sind, könnte ich mir auch eine Eichel-Familie vorstellen.
Visitenkarten und Briefpapier sollen alle wichtigen Infos enthalten, aber dabei sehr klar gehalten werden und nicht überladen sein. Mir ist ein schlichtes und ansprechendes Design wichtig. Es soll nicht verspielt sein.
Hier ist die Homepage:
www.eichel-gasthof-online.de
Info auf Briefpapier:
GASTHAUS EICHEL
Brennauer GmbH
Als Info auf Visitenkarte:
Gasthaus Eichel

```html
<!DOCTYPE html>
<html lang="de">
<head>
<meta charset="utf-8">
<title>Gasthaus Eichel – Geschäftsausstattung</title>
<link rel="stylesheet" href="https://fonts.googleapis.com/css2?family=Mukta:wght@300;400;500&display=swap">
<style>
  :root {
    --green: #8ea41a;
    --green-dark: #7f9416;
    --ink: #333333;
    --muted: #b4b4b4;
    --small: #8a8a8a;
    --paper: #ffffff;
    --backdrop: #ececec;
  }
  * { box-sizing: border-box; margin: 0; padding: 0; }
  html, body { width: 1200px; height: 848px; overflow: hidden; }
  body {
    position: relative;
    background: var(--backdrop);
    font-family: "Mukta", "Helvetica Neue", Arial, sans-serif;
    font-weight: 300;
    color: var(--muted);
  }
  .sheet { position: absolute; background: var(--paper); }

  /* brand lockup: plain square + name */
  .brand { display: flex; align-items: flex-end; gap: 8px; }
  .brand-square { background: var(--green); flex: none; }
  .brand-name { color: var(--green); font-weight: 400; line-height: 1; }

  /* standalone brand display */
  .brand-display { position: absolute; left: 895px; top: 30px; }
  .brand-display .brand-square { width: 122px; height: 90px; }
  .brand-display .brand-name { font-size: 44px; }

  /* letterhead */
  .letterhead { left: 63px; top: 135px; width: 457px; height: 643px; }
  .letterhead .brand-square {
    position: absolute; right: 13px; top: 10px; width: 72px; height: 62px;
  }
  .letterhead .sender {
    position: absolute; right: 13px; top: 76px; text-align: right;
    font-size: 8.5px; line-height: 11px;
  }
  .sender .name { color: var(--green); font-weight: 500; letter-spacing: .2px; }
  .sender .gap { height: 9px; }
  .letterhead .footer-bar {
    position: absolute; left: 0; bottom: 24px; width: 65px; height: 8px; background: var(--green);
  }
  .letterhead .footer {
    position: absolute; left: 75px; right: 20px; bottom: 16px;
    display: flex; justify-content: space-between;
    font-size: 6px; line-height: 7.5px; color: var(--small); text-align: center;
  }

  /* business cards */
  .card-back { left: 585px; top: 200px; width: 300px; height: 175px; background: var(--green); }
  .card-back .brand { position: absolute; left: 10px; bottom: 12px; }
  .card-back .brand-square { width: 60px; height: 50px; background: var(--paper); }
  .card-back .brand-name { color: var(--paper); font-size: 24px; }

  .card-front { left: 800px; top: 305px; width: 280px; height: 170px; }
  .card-front .brand-square {
    position: absolute; left: 11px; bottom: 12px; width: 52px; height: 46px;
  }
  .card-front .contact {
    position: absolute; right: 15px; top: 70px; text-align: right;
    font-size: 7px; line-height: 9px;
  }
  .contact .name { color: var(--green); font-weight: 500; }
  .contact .gap { height: 8px; }

  /* envelope */
  .envelope { left: 569px; top: 556px; width: 521px; height: 222px; }
  .envelope .brand { position: absolute; left: 9px; top: 6px; }
  .envelope .brand-square { width: 58px; height: 50px; }
  .envelope .brand-name { font-size: 22px; }
  .envelope .web {
    position: absolute; right: 0; bottom: 24px; display: flex; align-items: center; gap: 3px;
    color: var(--green); font-size: 9px; font-weight: 400;
  }
  .envelope .web-bar { width: 39px; height: 8px; background: var(--green); }
</style>
</head>
<body>

  <div class="brand-display brand">
    <span class="brand-square"></span>
    <span class="brand-name">Eichel</span>
  </div>

  <section class="sheet letterhead" aria-label="Briefpapier">
    <span class="brand-square"></span>
    <address class="sender" style="font-style:normal">
      <div class="name">GASTHAUS EICHEL</div>
      <div>Brennauer GmbH</div>
      <div>Lindenplatz 3</div>
      <div>84512 Talbrunn</div>
      <div class="gap"></div>
      <div>Telefon 08631 4470</div>
      <div>info@eichel-gasthof-online.de</div>
      <div>www.eichel-gasthof-online.de</div>
    </address>
    <span class="footer-bar"></span>
    <div class="footer">
      <p>Steuernummer:<br>USt.-IdNr. DE xxx</p>
      <p>Handelsregister: ORT<br>Geschäftsführer: Vorname Nachname</p>
      <p>IBAN DExx xxxx xxxx xxxx xxxx xx<br>BIC XXXXXXX 1XXX</p>
      <p>Kontoinhaber:<br>Brennauer GmbH</p>
    </div>
  </section>

  <section class="sheet card-back" aria-label="Visitenkarte Rückseite">
    <div class="brand">
      <span class="brand-square"></span>
      <span class="brand-name">Eichel</span>
    </div>
  </section>

  <section class="sheet card-front" aria-label="Visitenkarte Vorderseite">
    <address class="contact" style="font-style:normal">
      <div class="name">Gasthaus Eichel</div>
      <div class="name">Talbrunn im Rottal</div>
      <div class="gap"></div>
      <div>Brennauer GmbH</div>
      <div>Lindenplatz 3</div>
      <div>84512 Talbrunn</div>
      <div class="gap"></div>
      <div>Tel. 08631 4470</div>
      <div class="gap"></div>
      <div>www.eichel-gasthof-online.de</div>
      <div>info@eichel-gasthof-online.de</div>
    </address>
    <span class="brand-square"></span>
  </section>

  <section class="sheet envelope" aria-label="Briefumschlag">
    <div class="brand">
      <span class="brand-square"></span>
      <span class="brand-name">Eichel</span>
    </div>
    <div class="web">
      <span>www.eichel-gasthof-online.de</span>
      <span class="web-bar"></span>
    </div>
  </section>

</body>
</html>
```